New design for our thank you cards *

We need Thank You card designs for our mortgage broking company "Harrowgate Lending". We have an existing design and need a revamp of these. We are a boutique broking firm and would like "thank you" cards to send to our clients who refer new clients.

We are a referral-based business, our success and longevity is inextricably linked to the advice and service we provide our clients and referral partners.

Industry/Entity Type

Mortgage Brokerage

Colors
0792cd
0255a3
3176b5
33a6d7
85acd3
85cae6
cee9f5
cedeed
ffffff

Requirements
Must have
• our logo on the front 7 thank you & print on the back

```html
<!DOCTYPE html>
<html lang="en">
<head>
<meta charset="utf-8">
<title>Harrowgate Lending – Thank You Card</title>
<link rel="stylesheet" href="https://fonts.googleapis.com/css2?family=Pinyon+Script&family=Titillium+Web:wght@600&display=swap">
<style>
  :root {
    --page: #ffffff;
    --linen: #efe8d2;
    --linen-light: #f6f1e1;
    --bird-deep: #0255a3;
    --bird-mid: #3176b5;
    --bird-bright: #0792cd;
    --note: #ffffff;
    --note-edge: #e6e8ea;
    --script: #2a3f9e;
    --brand-ink: #1c1c24;
    --brand-mark: #0792cd;
  }
  * { margin: 0; padding: 0; box-sizing: border-box; }
  html, body {
    width: 1200px; height: 1200px; overflow: hidden;
    background: var(--page);
  }
  .card {
    position: absolute;
    left: 50px; top: 210px;
    width: 1100px; height: 780px;
    overflow: hidden;
  }
  .card__texture {
    position: absolute; inset: 0;
    background: linear-gradient(135deg, var(--linen-light), var(--linen));
  }
  .card__bird {
    position: absolute;
    left: -60px; top: 120px;
    width: 470px; height: 700px;
    border-radius: 48% 52% 30% 40% / 30% 34% 20% 30%;
    background: radial-gradient(circle at 65% 20%, var(--bird-bright), var(--bird-mid) 45%, var(--bird-deep));
  }
  .note {
    position: absolute;
    left: 172px; top: 208px;
    width: 585px; height: 413px;
    transform: rotate(-39.5deg);
    background: linear-gradient(120deg, var(--note) 40%, var(--note-edge));
    box-shadow: -18px 22px 30px rgba(0,0,0,0.55);
  }
  .note__greeting {
    position: absolute; inset: 0;
    display: flex; flex-direction: column; justify-content: center;
    font-family: "Pinyon Script", cursive;
    color: var(--script);
    line-height: 0.9;
  }
  .note__greeting span { display: block; font-size: 150px; }
  .note__line--first { padding-left: 40px; }
  .note__line--second { padding-left: 230px; }
  .brand {
    position: absolute;
    left: 612px; top: 596px;
    display: flex; align-items: center; gap: 16px;
  }
  .brand__square {
    width: 84px; height: 84px;
    background: var(--brand-mark);
  }
  .brand__name {
    font-family: "Titillium Web", sans-serif;
    font-weight: 600;
    color: var(--brand-ink);
    font-size: 38px;
    line-height: 1.05;
    letter-spacing: 2px;
    text-transform: uppercase;
  }
</style>
</head>
<body>
  <main class="card">
    <div class="card__texture" role="img" aria-label="Woven cream linen texture background"></div>
    <div class="card__bird" role="img" aria-label="Painted bluebird illustration holding the note in its beak"></div>
    <div class="note">
      <p class="note__greeting">
        <span class="note__line--first">Thank</span>
        <span class="note__line--second">You!</span>
      </p>
    </div>
    <div class="brand">
      <div class="brand__square"></div>
      <p class="brand__name">Harrowgate<br>Lending</p>
    </div>
  </main>
</body>
</html>
```